Martin & Ilse Crowther
WE HAVE MOVED
The address of our new home is
Fern Hollow
48 Wexcombe Lane
Thornby on Wyle
Warwickshire
B97 3LT
Tel: 07912 408716
Email: martin@kelvo.uk.com

```html
<!DOCTYPE html>
<html lang="en">
<head>
<meta charset="utf-8">
<title>We Have Moved – Martin &amp; Ilse Crowther</title>
<link rel="stylesheet" href="https://fonts.googleapis.com/css2?family=Barlow:wght@600;700&family=Kaushan+Script&display=swap">
<style>
  :root {
    --backdrop: #3a3a3a;
    --card-orange: #ff6a06;
    --ink-white: #ffffff;
  }
  * { margin: 0; padding: 0; box-sizing: border-box; }
  html, body {
    width: 1200px;
    height: 900px;
    overflow: hidden;
    background: var(--backdrop);
  }
  .canvas {
    position: relative;
    width: 1200px;
    height: 900px;
    font-family: "Barlow", "Arial Narrow", sans-serif;
    color: var(--ink-white);
  }
  .moving-card {
    position: absolute;
    left: 116px;
    top: 106px;
    width: 970px;
    height: 686px;
    border-radius: 62px;
    background: var(--card-orange);
  }
  .route-line {
    position: absolute;
    inset: 0;
    width: 1200px;
    height: 900px;
  }
  .household-name {
    position: absolute;
    left: 208px;
    top: 160px;
    font-size: 55px;
    font-weight: 700;
    line-height: 1;
    padding-right: 8px;
    background: var(--card-orange);
    white-space: nowrap;
  }
  .headline-script {
    position: absolute;
    left: 0;
    width: 1210px;
    top: 232px;
    text-align: center;
    font-family: "Kaushan Script", cursive;
    font-size: 124px;
    line-height: 1;
  }
  .headline-block {
    position: absolute;
    left: 0;
    width: 1214px;
    top: 352px;
    text-align: center;
    font-size: 250px;
    font-weight: 700;
    line-height: 1;
    letter-spacing: 2px;
  }
  .address-heading {
    position: absolute;
    left: 249px;
    top: 626px;
    font-size: 26px;
    font-weight: 700;
    line-height: 1;
    letter-spacing: 0.3px;
  }
  .address-lines {
    position: absolute;
    left: 250px;
    top: 658px;
    font-size: 19px;
    font-weight: 600;
    line-height: 26.5px;
    font-style: normal;
  }
  .pin-icon {
    position: absolute;
    left: 189px;
    top: 695px;
    width: 44px;
    height: 58px;
  }
  .contact-phone {
    position: absolute;
    right: 190px;
    top: 690px;
    display: flex;
    align-items: center;
    gap: 6px;
    font-size: 47px;
    font-weight: 700;
    line-height: 1;
    letter-spacing: 0.5px;
  }
  .phone-icon { width: 42px; height: 24px; }
  .contact-email {
    position: absolute;
    left: 680px;
    top: 738px;
    display: flex;
    align-items: center;
    gap: 17px;
    font-size: 19px;
    font-weight: 600;
    line-height: 1;
  }
  .mail-icon { width: 22px; height: 15px; }
</style>
</head>
<body>
<main class="canvas">
  <section class="moving-card" aria-label="Change of address card"></section>

  <svg class="route-line" viewBox="0 0 1200 900" aria-hidden="true">
    <path d="M620 196 H1006 Q1033 196 1033 223 V571 Q1033 597 1006 597 H237 Q210 597 210 624 V680"
          fill="none" stroke="var(--ink-white)" stroke-width="4" stroke-dasharray="22 14" stroke-linecap="round"/>
  </svg>

  <h2 class="household-name">Martin &amp; Ilse Crowther</h2>
  <p class="headline-script">We Have</p>
  <h1 class="headline-block">MOVED</h1>

  <h3 class="address-heading">THE ADDRESS OF OUR NEW HOME IS</h3>

  <svg class="pin-icon" viewBox="0 0 44 58" aria-hidden="true">
    <path d="M22 0 C9.8 0 0 9.6 0 21.6 C0 36 22 58 22 58 C22 58 44 36 44 21.6 C44 9.6 34.2 0 22 0 Z M22 29 A8 8 0 1 1 22 13 A8 8 0 1 1 22 29 Z"
          fill="var(--ink-white)" fill-rule="evenodd"/>
  </svg>

  <address class="address-lines">
    Fern Hollow 48 Wexcombe Lane<br>
    Thornby on Wyle<br>
    Warwickshire<br>
    B97 3LT
  </address>

  <p class="contact-phone">
    <svg class="phone-icon" viewBox="0 0 42 24" aria-hidden="true">
      <path d="M2 9 C8 1 34 1 40 9 L40 13 L31 13 L29 8 C24 6 18 6 13 8 L11 13 L2 13 Z" fill="var(--ink-white)"/>
      <path d="M9 14 L15 10 L27 10 L33 14 L35 23 L7 23 Z" fill="var(--ink-white)"/>
      <circle cx="21" cy="17" r="4" fill="var(--card-orange)"/>
    </svg>
    <span class="phone-number">07912 408716</span>
  </p>

  <p class="contact-email">
    <svg class="mail-icon" viewBox="0 0 22 15" aria-hidden="true">
      <rect x="0" y="0" width="22" height="15" rx="1.5" fill="var(--ink-white)"/>
      <path d="M1 1.5 L11 9 L21 1.5" fill="none" stroke="var(--card-orange)" stroke-width="1.8"/>
    </svg>
    <span class="email-address">martin@kelvo.uk.com</span>
  </p>
</main>
</body>
</html>
```